Business Card Design Project- Removalist

I would like to surprise my husband to be with a different type of wedding present. His brother (who he owned a removalist business with) suddenly passed away from cancer recently and he has changed his business name to 'RTB' (which stands for Raising Tom Bright; but the full name doesn't need to be on the business card as it is more of a personal business name). To celebrate the new business I would like to get him some business cards made.
I would like the business name to be listed as 'RTB' and somewhere on the card I would like 'Sydney wide removals and relocation services'. I would like it to be obvious from the front of the card that it is a removalist business card. If a truck or some other feature that makes it look like a removalist business card could added it would be appreciated.
I don't mind what colours are used, but I would like the colour blue to feature somewhere in the design. It can be bright and fun, which is how Tom was.
I will also need the company's email address and phone number listed
The email address is: rtbremovals@quillpost.example
The contact number is: 0417 282 934
I don't need a contact name listed on the card, but perhaps 'Owned and operated by the Pendleworth family' could be added near the contact details in small font.
Thank you very much for considering this project!
Kind regards,
Fiona
Updates
Could you please change the mobile contact number to 0417 282 934. This is the only contact phone number required on the card now.
Thank you!

```html
<!DOCTYPE html>
<html lang="en">
<head>
<meta charset="utf-8">
<title>RTB Removals – Business Card</title>
<link rel="stylesheet" href="https://fonts.googleapis.com/css2?family=Arimo:wght@400;700&display=swap">
<style>
  :root {
    --backdrop: #3b3b3b;
    --card-blue: #0b5a94;
    --ink-white: #ffffff;
    --truck-light: #e6e6e6;
    --truck-mid: #b9b9b9;
  }
  * { box-sizing: border-box; margin: 0; padding: 0; }
  html, body {
    width: 1200px;
    height: 750px;
    overflow: hidden;
    background: var(--backdrop);
  }
  .stage {
    position: relative;
    width: 1200px;
    height: 750px;
    display: flex;
    align-items: center;
    justify-content: center;
  }
  .business-card {
    position: relative;
    width: 358px;
    height: 646px;
    background: var(--card-blue);
    color: var(--ink-white);
    font-family: "Arimo", Arial, sans-serif;
  }
  .truck-illustration {
    position: absolute;
    left: 75px;
    top: 63px;
    width: 201px;
    height: 161px;
    border-radius: 6px;
    background: linear-gradient(160deg, var(--truck-light) 0%, var(--truck-mid) 100%);
  }
  .brand-name {
    position: absolute;
    left: 0;
    right: 0;
    top: 268px;
    text-align: center;
    font-size: 92px;
    font-weight: 700;
    letter-spacing: 10px;
    line-height: 1;
  }
  .tagline {
    position: absolute;
    left: 0;
    right: 0;
    top: 358px;
    text-align: center;
    font-size: 13px;
    font-weight: 700;
  }
  .contact-list {
    position: absolute;
    left: 39px;
    top: 530px;
    list-style: none;
  }
  .contact-item {
    display: flex;
    align-items: center;
    gap: 12px;
    height: 26px;
    font-size: 18px;
  }
  .contact-icon { width: 34px; height: 22px; flex: none; }
  .ownership-note {
    position: absolute;
    left: 0;
    right: 0;
    top: 588px;
    text-align: center;
    font-size: 13px;
  }
</style>
</head>
<body>
  <main class="stage">
    <article class="business-card">
      <div class="truck-illustration" role="img" aria-label="Illustration of a white box removals truck"></div>

      <h1 class="brand-name">RTB</h1>
      <p class="tagline">Sydney wide removals and relocation services</p>

      <ul class="contact-list">
        <li class="contact-item">
          <svg class="contact-icon" viewBox="0 0 34 22" aria-hidden="true">
            <path d="M3 8 Q17 -1 31 8 L28 11 L23 9 L23 6 Q17 4 11 6 L11 9 L6 11 Z" fill="none" stroke="#fff" stroke-width="1.6" stroke-linejoin="round"/>
            <rect x="7" y="11" width="20" height="10" rx="1.5" fill="none" stroke="#fff" stroke-width="1.6"/>
            <circle cx="13" cy="15" r="1" fill="#fff"/><circle cx="17" cy="15" r="1" fill="#fff"/><circle cx="21" cy="15" r="1" fill="#fff"/>
            <circle cx="13" cy="18.5" r="1" fill="#fff"/><circle cx="17" cy="18.5" r="1" fill="#fff"/><circle cx="21" cy="18.5" r="1" fill="#fff"/>
          </svg>
          <span>0417 282 934</span>
        </li>
        <li class="contact-item">
          <svg class="contact-icon" viewBox="0 0 34 22" aria-hidden="true">
            <rect x="3" y="2" width="28" height="18" fill="none" stroke="#fff" stroke-width="1.6"/>
            <path d="M3 2 L17 13 L31 2" fill="none" stroke="#fff" stroke-width="1.6"/>
          </svg>
          <span>rtbremovals@quillpost.example</span>
        </li>
      </ul>

      <p class="ownership-note">Owned and operated by the Pendleworth family</p>
    </article>
  </main>
</body>
</html>
```